Hal's Remedies Business Card Design Project

I need a business card designed for my pharmacy Hal's Remedies. I would like just the logo on one side, maybe with black background and white lettering. The other side I would also like to include my logo which is attached. Also, please include my name and the following information:
Hal Norwick Owner/Pharm D.
Business address is 7163 N Birch Rd Sioux Falls, SD 57291.
Phone number is 605-318-6027 and fax # is 605-318-6031.
my email address is hal@halsremedies.example.
My website is www.halsremedies.example.
My business hours are Monday-Friday 8am-7 pm. Saturday 8am-12 pm. Sunday Closed.
I would like the design to include my logo colors, black, white, and neon green. Silver may be added as a highlight. Thanks.
Pharmacy
See above in product description

```html
<!DOCTYPE html>
<html lang="en">
<head>
<meta charset="utf-8">
<title>Hal's Remedies – Business Card</title>
<link href="https://fonts.googleapis.com/css2?family=Open+Sans:wght@400;600;700&display=swap" rel="stylesheet">
<style>
  :root {
    --stage: #e9e7e4;
    --card-black: #000000;
    --white: #ffffff;
    --neon-green: #9fd42a;
    --silver-light: #ffffff;
    --silver-mid: #e6e6e6;
    --silver-dark: #b9b9b9;
    --ink: #2a2a2a;
    --icon: #1e1e1e;
  }
  * { box-sizing: border-box; margin: 0; padding: 0; }
  html, body {
    width: 1200px; height: 440px; overflow: hidden;
    background: var(--stage);
    font-family: "Open Sans", sans-serif;
  }
  .canvas { position: relative; width: 1200px; height: 440px; }
  .card {
    position: absolute; top: 62px;
    width: 550px; height: 322px;
    box-shadow: 0 3px 10px rgba(0,0,0,0.25);
    overflow: hidden;
  }
  /* Front */
  .card-front {
    left: 43px; background: var(--card-black);
    display: flex; align-items: center; justify-content: center; gap: 22px;
  }
  .brand-dot {
    width: 36px; height: 36px; border-radius: 50%;
    background: var(--neon-green);
  }
  .brand-name {
    color: var(--white); font-weight: 700; font-size: 40px;
    letter-spacing: -0.5px;
  }
  /* Back */
  .card-back {
    left: 607px;
    background: linear-gradient(160deg, var(--silver-light) 0%, var(--silver-mid) 45%, var(--silver-dark) 100%);
  }
  .product-photo {
    position: absolute; left: 0; top: 0; width: 100px; height: 100%;
    background: linear-gradient(170deg, #f2a36b 0%, #e86a8e 25%, #f5d36a 45%, #7fb3de 65%, #f1ede6 82%, #f2b070 100%);
  }
  .contact-name {
    position: absolute; left: 186px; top: 15px;
    font-size: 18.5px; color: var(--ink);
  }
  .contact-list { position: absolute; left: 152px; top: 0; list-style: none; }
  .contact-item {
    position: absolute; left: 0; display: flex; align-items: center;
    font-size: 14.5px; color: var(--ink); white-space: nowrap;
  }
  .contact-item svg { width: 20px; height: 20px; margin-right: 14px; flex: none; }
  .hours {
    position: absolute; left: 186px; top: 268px;
    font-size: 14.5px; line-height: 19px; color: var(--ink);
  }
</style>
</head>
<body>
<div class="canvas">
  <section class="card card-front">
    <span class="brand-dot"></span>
    <span class="brand-name">Hal's Remedies</span>
  </section>

  <section class="card card-back">
    <div class="product-photo" role="img" aria-label="Photo of colourful pills and capsules"></div>
    <p class="contact-name">Hal Norwick Owner/Pharm D.</p>
    <ul class="contact-list">
      <li class="contact-item" style="top:61px">
        <svg viewBox="0 0 20 20" fill="var(--icon)"><path d="M10 1a6 6 0 0 0-6 6c0 4.5 6 12 6 12s6-7.5 6-12a6 6 0 0 0-6-6zm0 8.3A2.3 2.3 0 1 1 10 4.7a2.3 2.3 0 0 1 0 4.6z"/></svg>
        7163 N Birch Rd Sioux Falls, SD 57291.
      </li>
      <li class="contact-item" style="top:104px">
        <svg viewBox="0 0 20 20" fill="var(--icon)"><path d="M5.5 2.5l2.6 3.2-1.5 1.9c.9 2 2.5 3.6 4.5 4.5l1.9-1.5 3.2 2.6-1.4 2.8c-6.3-.4-11.3-5.4-11.7-11.7z"/></svg>
        605-318-6027
      </li>
      <li class="contact-item" style="top:143px">
        <svg viewBox="0 0 20 20" fill="var(--icon)"><path d="M6 2h8v4H6z"/><path d="M3 7h14a1 1 0 0 1 1 1v6h-3v-2H5v2H2V8a1 1 0 0 1 1-1z"/><path d="M6 13h8v5H6z"/></svg>
        605-318-6031.
      </li>
      <li class="contact-item" style="top:185px">
        <svg viewBox="0 0 20 20" fill="none" stroke="var(--icon)" stroke-width="1.4"><rect x="2" y="4.5" width="16" height="11"/><path d="M2 4.5l8 6.5 8-6.5"/></svg>
        hal@halsremedies.example.
      </li>
      <li class="contact-item" style="top:225px">
        <svg viewBox="0 0 20 20" fill="none" stroke="var(--icon)" stroke-width="1.5"><circle cx="10" cy="10" r="8" fill="var(--icon)"/><ellipse cx="10" cy="10" rx="3.5" ry="8" stroke="#ddd"/><path d="M2 10h16M3.5 6h13M3.5 14h13" stroke="#ddd" stroke-width="1"/></svg>
        www.halsremedies.example.
      </li>
    </ul>
    <p class="hours">Monday-Friday 8am-7 pm. Saturday 8am-12 pm.<br>Sunday Closed</p>
  </section>
</div>
</body>
</html>
```